Email marketing template

Job type:
Email marketing

Task description:
We would like to send an E-card to our clients wishing them a Merry Christmas

Copy for email marketing:

Seasons Greetings from everyone at PRV…

This year we are supporting our chosen charities by making a donation to help them continue their hard work making a difference. Have a look at our website to find more about the chosen charities we are supporting this Christmas:

http://www.morvenhale.com/Our-Approach/Brightloom

Best wishes,

The PRV team

Logo text:
PRV

Descriptive words:
Fun
Playful
Bold
Festive

Deadline:
Monday 16th December

Other information:
We will require you to provide us with HTML coding and uploading to Mail Chimp. We will then process payment upon testing final materials.

Industry/Entity Type

Marketing

```html
<!DOCTYPE html>
<html lang="en">
<head>
<meta charset="utf-8">
<title>Seasons Greetings from everyone at PRV</title>
<link rel="stylesheet" href="https://fonts.googleapis.com/css2?family=Arimo:wght@400;700&family=Dancing+Script:wght@600;700&display=swap">
<style>
  :root {
    --page-bg: #ffffff;
    --body-text: #4a4a4a;
    --caption-text: #333333;
    --link-blue: #3aa3cf;
    --night-top: #05101c;
    --night-blue: #12395c;
    --deep-blue: #0d2238;
    --ember: #6e3c16;
    --candle-gold: #c9842e;
    --logo-square: #1e8fd0;
    --white: #ffffff;
  }
  * { box-sizing: border-box; margin: 0; padding: 0; }
  html, body {
    width: 1200px;
    height: 984px;
    overflow: hidden;
    background: var(--page-bg);
  }
  .ecard {
    position: relative;
    width: 1200px;
    height: 984px;
    font-family: "Arimo", Arial, sans-serif;
  }
  .hero {
    position: absolute;
    left: 36px;
    top: 20px;
    width: 1124px;
    height: 546px;
    overflow: hidden;
  }
  .hero-photo {
    position: absolute;
    inset: 0;
    background: linear-gradient(180deg,
      var(--night-top) 0%,
      var(--night-top) 25%,
      var(--night-blue) 45%,
      var(--deep-blue) 62%,
      var(--ember) 82%,
      var(--candle-gold) 100%);
  }
  .hero-greeting {
    position: absolute;
    left: 112px;
    top: 14px;
    font-family: "Dancing Script", cursive;
    font-weight: 700;
    color: var(--white);
    font-size: 112px;
    line-height: 100px;
  }
  .hero-greeting .line-one { display: block; margin-left: 76px; }
  .hero-greeting .line-two { display: block; }
  .brand {
    position: absolute;
    left: 560px;
    top: 82px;
    display: flex;
    align-items: flex-end;
    gap: 28px;
  }
  .brand-square {
    width: 86px;
    height: 86px;
    margin-bottom: 14px;
    background: var(--logo-square);
  }
  .brand-text { color: var(--white); display: flex; flex-direction: column; align-items: flex-end; }
  .brand-tagline {
    font-size: 16px;
    margin-bottom: -4px;
    margin-right: -30px;
  }
  .brand-name {
    font-size: 112px;
    font-weight: 400;
    line-height: 108px;
    letter-spacing: 2px;
  }
  .caption {
    position: absolute;
    left: 36px;
    top: 584px;
    font-size: 18px;
    color: var(--caption-text);
  }
  .message {
    position: absolute;
    left: 36px;
    top: 648px;
    width: 1060px;
    font-size: 27px;
    line-height: 44px;
    color: var(--body-text);
  }
  .message a { color: var(--link-blue); text-decoration: underline; }
  .sign-off { margin-top: 44px; }
</style>
</head>
<body>
  <main class="ecard">
    <section class="hero">
      <div class="hero-photo" role="img" aria-label="Festive photo of a glowing tea light candle, a star and baubles on golden glitter against a dark blue background"></div>
      <h1 class="hero-greeting"><span class="line-one">Seasons</span><span class="line-two">Greetings</span></h1>
      <div class="brand">
        <span class="brand-square"></span>
        <span class="brand-text">
          <span class="brand-tagline">from everyone at</span>
          <span class="brand-name">PRV</span>
        </span>
      </div>
    </section>
    <p class="caption">Your text caption goes here</p>
    <div class="message">
      <p>This year we are supporting our chosen charities by making a donation to help them continue their hard work making a difference. Have a look at our website to find more about the chosen charities we are supporting this Christmas:<br>
      <a href="http://www.morvenhale.com/Our-Approach/Brightloom">http://www.morvenhale.com/Our-Approach/Brightloom</a></p>
      <p class="sign-off">Best wishes,<br>The PRV team</p>
    </div>
  </main>
</body>
</html>
```